Business card for Verano Living

Hi again, I need a business card for my Verano Living business you have been working on with the following information:

Clara Hollis
Director
m. 0412 736 258
e. clara@veranoliving-example.com.au
w. www.veranoliving-example.com.au

Maybe you could use the original design (using both the green & white) and where the white box is you could include the above details (name / mobile / etc) - Perhaps the 'i' in Clara could be the bow tie again?

Then the back could be green with black writing stating:

Services Offered:

* Personal Assistant Concierge
* Decluttering Concierge
* Home Management Concierge
* FIFO Concierge
* Events Concierge
* Leisure & Travel Concierge
* Seasonal Concierge
* Professional Concierge

Many thanks
Updates

Hi Everyone I'm really sorry but I am working with just one designer on this brief, thank you for your work and apologies for my error.

Industry/Entity Type

Business

```html
<!DOCTYPE html>
<html lang="en">
<head>
<meta charset="utf-8">
<title>Verano Living – Business Card</title>
<link rel="stylesheet" href="https://fonts.googleapis.com/css2?family=Titillium+Web:wght@300;400;600&family=Pinyon+Script&display=swap">
<style>
  :root {
    --backdrop: #ece8e2;
    --green: #64a43a;
    --green-light: #7cb84a;
    --green-dark: #568f30;
    --brand-tint: #b4e06a;
    --paper: #ffffff;
    --ink: #111111;
    --on-green: #ffffff;
    --sans: "Titillium Web", Arial, sans-serif;
    --script: "Pinyon Script", cursive;
  }
  * { box-sizing: border-box; margin: 0; padding: 0; }
  html, body { width: 1200px; height: 800px; overflow: hidden; }
  body {
    background: var(--backdrop);
    position: relative;
    font-family: var(--sans);
  }
  p { line-height: 1.1; white-space: nowrap; }
  .card {
    position: absolute;
    top: 250px;
    width: 520px;
    height: 298px;
    overflow: hidden;
    box-shadow: 0 6px 18px rgba(0,0,0,0.18);
  }
  .card--front { left: 50px; background: var(--paper); }
  .card--back {
    left: 630px;
    background: linear-gradient(135deg, var(--green-light), var(--green-dark));
  }

  /* Front */
  .front__top {
    position: absolute; left: 0; top: 0; width: 100%; height: 112px;
    background: linear-gradient(135deg, var(--green), var(--green-light));
  }
  .front__bottom {
    position: absolute; left: 0; bottom: 0; width: 100%; height: 40px;
    background: var(--green);
  }
  .brand {
    position: absolute;
    font-family: var(--sans);
    font-weight: 400;
    color: var(--brand-tint);
  }
  .tagline {
    position: absolute;
    font-family: var(--script);
    color: var(--ink);
  }
  .card--front .brand { left: 22px; top: 26px; font-size: 34px; }
  .card--front .tagline { left: 48px; top: 70px; font-size: 22px; }

  .contact-name {
    position: absolute; left: 262px; top: 122px;
    font-size: 30px; font-weight: 600; color: var(--green);
  }
  .contact-role {
    position: absolute; left: 332px; top: 158px;
    font-family: var(--script); font-size: 16px; color: var(--ink);
  }
  .contact-phone {
    position: absolute; left: 290px; top: 182px;
    font-size: 22px; color: var(--ink); letter-spacing: 0.5px;
  }
  .contact-email {
    position: absolute; left: 14px; top: 224px;
    font-size: 21px; color: var(--ink);
  }
  .contact-web {
    position: absolute; right: 16px; bottom: 9px;
    font-size: 18px; color: var(--on-green);
  }

  /* Back */
  .card--back .brand { left: 70px; top: 52px; font-size: 48px; }
  .card--back .tagline { left: 110px; top: 108px; font-size: 28px; }
  .services {
    position: absolute; left: 30px; right: 30px; top: 166px;
    text-align: center;
    font-size: 17px; line-height: 23px;
    color: var(--on-green);
    list-style: none;
  }
  .services li { display: inline; }
  .services li + li::before { content: " | "; }
</style>
</head>
<body>
  <section class="card card--front" aria-label="Business card front">
    <div class="front__top"></div>
    <div class="front__bottom"></div>
    <p class="brand">Verano Living</p>
    <p class="tagline">Your Personal Concierge</p>
    <p class="contact-name">Clara Hollis</p>
    <p class="contact-role">Director</p>
    <p class="contact-phone">0412 736 258</p>
    <p class="contact-email">clara@veranoliving-example.com.au</p>
    <p class="contact-web">www.veranoliving-example.com.au</p>
  </section>

  <section class="card card--back" aria-label="Business card back">
    <p class="brand">Verano Living</p>
    <p class="tagline">Your Personal Concierge</p>
    <ul class="services">
      <li>Personal Assistant Concierge</li><li>Decluttering Concierge</li><li>Home Management Concierge</li><li>FIFO Concierge</li><li>Events Concierge</li><li>Leisure &amp; Travel Concierge</li><li>Seasonal Concierge</li><li>Professional Concierge</li>
    </ul>
  </section>
</body>
</html>
```